BUSINESS CONSULTING

Would like a page design that would reflect "flow" effect that denotes moving around obstacles and logo webpage for BREXA Consulting. We provide business consulting in the areas of training/facilitation, Leadership Coaching and Development, Process Improvement and Employee On-boarding and Authorization.

Need skeletal designed to be populated at a later date.

```html
<!DOCTYPE html>
<html lang="en">
<head>
<meta charset="utf-8">
<title>BREXA Consulting</title>
<link href="https://fonts.googleapis.com/css2?family=PT+Sans+Narrow:wght@400;700&family=Open+Sans:wght@400;600&display=swap" rel="stylesheet">
<style>
:root{
  --green:#12994a;
  --green-dark:#0d7a38;
  --grey-text:#555a5e;
  --navy:#2f3b4a;
  --orange:#f39a1e;
  --orange-dark:#e07f0c;
  --page:#eff1f0;
  --footer:#e5e6e6;
  --white:#ffffff;
}
*{margin:0;padding:0;box-sizing:border-box}
html,body{width:1024px;height:1200px;overflow:hidden}
body{position:relative;background:var(--page);font-family:"Open Sans",sans-serif;color:var(--grey-text)}
.abs{position:absolute}

/* header */
.site-header{left:0;top:0;width:1024px;height:84px;background:var(--white);border-top:3px solid #bdbdbd}
.phone-tab{left:605px;top:0;width:288px;height:26px;background:#f1f1f1;border-radius:0 0 8px 8px;display:flex;align-items:center;justify-content:center;gap:6px;font-family:"PT Sans Narrow",sans-serif;font-weight:700;font-size:13px;color:#6a6f73}
.phone-tab b{color:var(--green)}
.logo{left:116px;top:26px;font-family:"PT Sans Narrow",sans-serif;font-weight:700;font-size:27px;color:var(--green);letter-spacing:-.3px}
.main-nav{left:494px;top:43px;display:flex;gap:27px;font-family:"PT Sans Narrow",sans-serif;font-weight:700;font-size:13px;letter-spacing:.5px;color:#6b6f75}
.main-nav .active{color:var(--navy)}
.quote-btn{left:775px;top:35px;width:112px;height:36px;background:linear-gradient(#f7ab3a,var(--orange-dark));border-radius:3px;display:flex;align-items:center;gap:8px;padding-left:13px;font-family:"PT Sans Narrow",sans-serif;font-weight:700;font-size:12px;line-height:12px;color:var(--white);letter-spacing:.5px}

/* hero */
.hero{left:0;top:84px;width:1024px;height:397px;background:linear-gradient(180deg,#b9b2b4 0%,#c8a28a 35%,#8b7a6c 55%,#5c5650 80%,#4a4846 100%)}
.hero-title{left:112px;top:332px;font-family:"PT Sans Narrow",sans-serif;font-weight:700;font-size:35px;line-height:41px;color:var(--white);letter-spacing:-.8px;text-shadow:0 1px 3px rgba(0,0,0,.4)}
.arrow{width:38px;height:38px;border-radius:50%;display:flex;align-items:center;justify-content:center;border:3px solid rgba(255,255,255,.35)}
.arrow.prev{left:77px;top:235px;background:var(--green)}
.arrow.next{left:903px;top:235px;background:#3a3d40}

/* services panel */
.panel{left:108px;top:439px;width:803px;height:306px;background:var(--white);border-radius:3px;box-shadow:0 10px 30px rgba(0,0,0,.12)}
.card{top:470px;width:176px;height:233px;background:var(--white);border-top:4px solid #8a8a8a;box-shadow:0 1px 4px rgba(0,0,0,.25)}
.card h3{font-family:"PT Sans Narrow",sans-serif;font-weight:700;font-size:11px;line-height:14px;color:var(--green);text-align:center;height:46px;padding-top:13px}
.card .thumb{margin:0 0 0 13px;width:149px;height:78px}
.card p{font-size:8.6px;line-height:11.3px;color:#4a4e52;padding:20px 12px 0 14px;height:76px}
.card a{display:block;padding-left:14px;font-family:"PT Sans Narrow",sans-serif;font-size:8.5px;color:var(--navy);text-decoration:underline;letter-spacing:.3px}

/* welcome */
.welcome-img{left:136px;top:757px;width:158px;height:210px;background:linear-gradient(160deg,#9fb4a2 0%,#6e8c6a 40%,#c7332d 70%,#5b5f55 100%)}
.welcome-title{left:311px;top:749px;font-family:"PT Sans Narrow",sans-serif;font-weight:700;font-size:21px;color:#5e6266}
.welcome-title span,.services-title span{color:var(--green)}
.welcome-text{left:313px;top:783px;font-size:9.6px;line-height:16px;color:#62666a;white-space:nowrap}
.welcome-text p+p{margin-top:16px}
.learn-btn{left:311px;top:938px;width:64px;height:28px;border:1px solid #cfcfcf;border-radius:3px;background:linear-gradient(#f8f8f8,#e4e4e4);font-size:8.5px;color:#777;display:flex;align-items:center;justify-content:center}
.services-title{left:649px;top:749px;font-family:"PT Sans Narrow",sans-serif;font-weight:700;font-size:21px;color:#5e6266}
.service-list{left:649px;top:782px;list-style:none}
.service-list li{display:flex;align-items:center;gap:10px;height:24px;font-size:12px;color:#62666a}

/* footer */
.site-footer{left:0;top:1017px;width:1024px;height:147px;background:var(--footer);border-top:1px solid #d6d6d6}
.footer-logo{left:153px;top:1071px;font-family:"PT Sans Narrow",sans-serif;font-weight:700;font-size:15px;color:var(--green)}
.footer-col h4{font-size:11.5px;font-weight:600;color:#5a5e62;margin-bottom:9px}
.footer-col ul{list-style:none}
.footer-col li{font-size:8.5px;color:#777;height:19px;display:flex;align-items:center;gap:7px;letter-spacing:.3px}
.footer-col li.current{color:var(--green)}
.tri{width:0;height:0;border-left:3px solid #888;border-top:3px solid transparent;border-bottom:3px solid transparent}
.contact-col li{height:24px;gap:10px}
.social{display:flex;gap:8px}
.social span{width:28px;height:28px;border-radius:3px;display:block;box-shadow:0 1px 2px rgba(0,0,0,.3)}
.bottom-bar{left:0;top:1164px;width:1024px;height:36px;background:var(--green-dark);display:flex;align-items:center;justify-content:space-between;padding:0 133px;font-size:8.5px;color:#5fb27f}
</style>
</head>
<body>

<header class="abs site-header"></header>
<div class="abs phone-tab">
  <svg width="16" height="16" viewBox="0 0 16 16"><circle cx="8" cy="8" r="7" fill="none" stroke="#12994a" stroke-width="1.4"/><path d="M5.5 4.5c-.6.6-.5 2 .7 3.5s2.8 2.5 3.6 1.9l.7-.7-1.3-1.2-.7.5c-.6-.3-1.3-1-1.6-1.6l.5-.7-1.2-1.3z" fill="#12994a"/></svg>
  FOR INQUIRIES, CALL US: <b>1-800-555-01470</b>
</div>
<div class="abs logo">BREXA Consulting</div>
<nav class="abs main-nav">
  <span class="active">HOME</span><span>ABOUT US</span><span>SERVICES</span><span>CONTACT</span>
</nav>
<div class="abs quote-btn">
  <svg width="16" height="20" viewBox="0 0 16 20"><rect x="1" y="1" width="14" height="18" fill="none" stroke="#fff" stroke-width="1.5"/><path d="M4 6h8M4 9h8M4 12h8M4 15h5" stroke="#fff" stroke-width="1.3"/></svg>
  <span>GET YOUR<br>FREE QUOTE</span>
</div>

<section class="abs hero" role="img" aria-label="Photo of a white semi truck driving on a desert highway at sunset"></section>
<div class="abs hero-title">Providing Quality Specialized<br>Services in Global Logistics</div>
<div class="abs arrow prev"><svg width="8" height="10" viewBox="0 0 8 10"><path d="M6 1 2 5l4 4" fill="none" stroke="#fff" stroke-width="1.6"/></svg></div>
<div class="abs arrow next"><svg width="8" height="10" viewBox="0 0 8 10"><path d="M2 1l4 4-4 4" fill="none" stroke="#fff" stroke-width="1.6"/></svg></div>

<div class="abs panel"></div>

<article class="abs card" style="left:134px">
  <h3>Technology Solutions</h3>
  <div class="thumb" role="img" aria-label="Photo of a hand touching a glowing digital interface" style="background:linear-gradient(135deg,#123a6e,#3d86c6 50%,#0d2448)"></div>
  <p>Lorem ipsum dolor sit amet, consectetur adipisicing elit, sed do eiusmod tempor incididunt ut labore .</p>
  <a>READ MORE</a>
</article>
<article class="abs card" style="left:326px">
  <h3>Process Improvement &amp;<br>Consulting</h3>
  <div class="thumb" role="img" aria-label="Photo of business people meeting around a laptop" style="background:linear-gradient(135deg,#e8eaec,#b9bcc0 50%,#2f3236)"></div>
  <p>Lorem ipsum dolor sit amet, consectetur adipisicing elit, sed do eiusmod tempor incididunt ut labore .</p>
  <a>READ MORE</a>
</article>
<article class="abs card" style="left:518px">
  <h3>Distribution &amp;<br>Warehouse Management</h3>
  <div class="thumb" role="img" aria-label="Photo of colourful trucks beside a loaded pallet" style="background:linear-gradient(90deg,#c8262a,#f2d500 40%,#e6c200 70%,#c49a5c)"></div>
  <p>Lorem ipsum dolor sit amet, consectetur adipisicing elit, sed do eiusmod tempor incididunt ut labore .</p>
  <a>READ MORE</a>
</article>
<article class="abs card" style="left:710px">
  <h3>Value Added Services</h3>
  <div class="thumb" role="img" aria-label="Photo of hands working with documents, pen and keyboard" style="background:linear-gradient(135deg,#f1efec,#c9c4bd 55%,#54524f)"></div>
  <p>Lorem ipsum dolor sit amet, consectetur adipisicing elit, sed do eiusmod tempor incididunt ut labore .</p>
  <a>READ MORE</a>
</article>

<div class="abs welcome-img" role="img" aria-label="Photo of a red truck driving fast past trees"></div>
<h2 class="abs welcome-title">Welcome to <span>BREXA Consulting</span></h2>
<div class="abs welcome-text">
  <p>It is a long established fact that a reader will be distracted by the<br>readable content of a page when looking at its layout. The point<br>of using Lorem Ipsum is that it has a more-or-less normal distri-<br>bution of letters, as opposed to using 'Content here, content here',<br>making it look like readable English.</p>
  <p>Lorem ipsum dolor sit amet, consectetur adipisicing elit, sed do<br>eiusmod tempor incididunt ut labore et dolore magna aliqua. Ut<br>enim ad minim veniam, quis nostrud exercitation ullamco laboris</p>
</div>
<div class="abs learn-btn">Learn More</div>

<h2 class="abs services-title">Our <span>Services</span></h2>
<ul class="abs service-list">
  <li><svg width="15" height="15" viewBox="0 0 15 15"><circle cx="7.5" cy="7.5" r="7.5" fill="#12994a"/><path d="M6 4.5l3 3-3 3" fill="none" stroke="#fff" stroke-width="1.6"/></svg>Staffing and Management</li>
  <li><svg width="15" height="15" viewBox="0 0 15 15"><circle cx="7.5" cy="7.5" r="7.5" fill="#12994a"/><path d="M6 4.5l3 3-3 3" fill="none" stroke="#fff" stroke-width="1.6"/></svg>Warehouse Management</li>
  <li><svg width="15" height="15" viewBox="0 0 15 15"><circle cx="7.5" cy="7.5" r="7.5" fill="#12994a"/><path d="M6 4.5l3 3-3 3" fill="none" stroke="#fff" stroke-width="1.6"/></svg>Distribution Solutions</li>
  <li><svg width="15" height="15" viewBox="0 0 15 15"><circle cx="7.5" cy="7.5" r="7.5" fill="#12994a"/><path d="M6 4.5l3 3-3 3" fill="none" stroke="#fff" stroke-width="1.6"/></svg>Transportation Management Solutions</li>
  <li><svg width="15" height="15" viewBox="0 0 15 15"><circle cx="7.5" cy="7.5" r="7.5" fill="#12994a"/><path d="M6 4.5l3 3-3 3" fill="none" stroke="#fff" stroke-width="1.6"/></svg>Warehouse Management Solutions</li>
  <li><svg width="15" height="15" viewBox="0 0 15 15"><circle cx="7.5" cy="7.5" r="7.5" fill="#12994a"/><path d="M6 4.5l3 3-3 3" fill="none" stroke="#fff" stroke-width="1.6"/></svg>Inventory Management Solutions</li>
  <li><svg width="15" height="15" viewBox="0 0 15 15"><circle cx="7.5" cy="7.5" r="7.5" fill="#12994a"/><path d="M6 4.5l3 3-3 3" fill="none" stroke="#fff" stroke-width="1.6"/></svg>Consulting Services</li>
  <li><svg width="15" height="15" viewBox="0 0 15 15"><circle cx="7.5" cy="7.5" r="7.5" fill="#12994a"/><path d="M6 4.5l3 3-3 3" fill="none" stroke="#fff" stroke-width="1.6"/></svg>Value Added Services</li>
</ul>

<footer class="abs site-footer"></footer>
<div class="abs footer-logo">BREXA Consulting</div>
<div class="abs footer-col" style="left:321px;top:1042px">
  <h4>Navigation</h4>
  <ul><li><i class="tri"></i>Home</li><li><i class="tri"></i>About</li><li><i class="tri"></i>Services</li><li><i class="tri"></i>Contact</li></ul>
</div>
<div class="abs footer-col" style="left:448px;top:1042px">
  <h4>Services</h4>
  <ul><li class="current"><i class="tri"></i>Service</li><li><i class="tri"></i>Service</li><li><i class="tri"></i>Service</li><li><i class="tri"></i>Service</li></ul>
</div>
<div class="abs footer-col contact-col" style="left:576px;top:1042px">
  <h4>Contact Us</h4>
  <ul>
    <li><svg width="10" height="10" viewBox="0 0 10 10"><path d="M1.5 1c-1 1-.5 3 1.5 5s4 2.5 5 1.5l.5-.7-1.8-1.5-.9.6C5 5.5 4.4 5 4 4.2l.6-.9L3 1.5z" fill="#888"/></svg>+1800-555-0147</li>
    <li><svg width="11" height="8" viewBox="0 0 11 8"><rect x=".5" y=".5" width="10" height="7" fill="#888"/><path d="M.5.5l5 4 5-4" fill="none" stroke="#e5e6e6"/></svg>hello@brexamail.com</li>
    <li style="align-items:flex-start;height:auto;line-height:18px;padding-top:2px"><svg width="9" height="12" viewBox="0 0 9 12" style="margin-top:3px"><path d="M4.5 0A4.5 4.5 0 0 0 0 4.5C0 8 4.5 12 4.5 12S9 8 9 4.5A4.5 4.5 0 0 0 4.5 0z" fill="#888"/><circle cx="4.5" cy="4.5" r="1.6" fill="#e5e6e6"/></svg><span>Your Address, Your Country<br>Your Zip Code</span></li>
  </ul>
</div>
<div class="abs footer-col" style="left:750px;top:1042px">
  <h4>Social</h4>
  <div class="social">
    <span role="img" aria-label="Social network link" style="background:#3a5a98"></span>
    <span role="img" aria-label="Social network link" style="background:#2ea7e0"></span>
    <span role="img" aria-label="Social network link" style="background:#1d6fa5"></span>
    <span role="img" aria-label="Social network link" style="background:#d9402f"></span>
  </div>
</div>

<div class="abs bottom-bar">
  <span>Copyright 2014 © Brexa Consulting - All Rights Reserved</span>
  <span>Site Map &nbsp;&nbsp;•&nbsp;&nbsp; Privacy Policy</span>
</div>

</body>
</html>
```